Business Card Design Project

We have a logo, but would like to expand the use of it into a business card design. We are a B2B technology exchange platform for institutional investors to invest excess cash into short term assets matching their credit and pricing parameters. The assets are fractionalized and investors invest in portions.

Our customers are large, institutional, financial companies who are a bit traditional. We are high energy rebels with a cause...we are a disruptive technology and want to be viewed as a game changer but we need to present an image of trustworthiness and secure.

We are open not only to the image design but the material, die cut, etc. but want to stay in the traditional size of a business card.

We have other formats of the logo if needed. Our website is www.brambleharbor.com

I have posted a powerpoint template that we have been using.  This should not be considered the template we will use (after business cards we will have another project to incorporate business card design into powerpoint template) but just to give you a flavor of where we have been and have used in the past.

Target Market(s)

Institutional investors, asset managers, large fund institutions

Industry/Entity Type

Financial

Requirements
Must have
• Our logo
Traditional size
Nice to have
• unique use of logo, unique material, die cut, etc
Crisp, clean look
Use of both sides of card in a creative manner

```html
<!DOCTYPE html>
<html lang="en">
<head>
<meta charset="utf-8">
<title>Bramble Harbor – Business Card</title>
<link rel="stylesheet" href="https://fonts.googleapis.com/css2?family=Questrial&family=Open+Sans:wght@400&display=swap">
<style>
  :root {
    --page-bg: #ffffff;
    --card-bg: #ffffff;
    --card-border: #6d6e71;
    --ink: #4d4d4f;
    --ink-dark: #3a3a3c;
    --brand-grey: #636466;
    --brand-orange: #f7941d;
    --brand-peach: #fbd9b0;
    --icon-blue: #1a73b5;
  }
  html, body {
    margin: 0;
    padding: 0;
    width: 1200px;
    height: 900px;
    overflow: hidden;
    background: var(--page-bg);
  }
  .sheet {
    position: relative;
    width: 1200px;
    height: 900px;
    font-family: "Questrial", "Century Gothic", sans-serif;
    color: var(--ink);
  }
  .side-label {
    position: absolute;
    font-family: "Open Sans", Calibri, sans-serif;
    font-size: 31px;
    color: #111;
    margin: 0;
    font-weight: 400;
  }
  .side-label--front { left: 32px; top: 140px; }
  .side-label--back { left: 27px; top: 628px; }

  .card {
    position: absolute;
    box-sizing: border-box;
    border: 1px solid var(--card-border);
    background: var(--card-bg);
    overflow: hidden;
  }
  .card--front { left: 224px; top: 28px; width: 725px; height: 419px; }
  .card--back { left: 221px; top: 469px; width: 726px; height: 419px; }

  .phones {
    position: absolute;
    left: 36px;
    top: 32px;
    margin: 0;
    font-size: 17px;
    line-height: 28px;
  }
  .phones .kind { display: inline-block; width: 30px; }

  .identity {
    position: absolute;
    right: 37px;
    top: 50px;
    text-align: right;
    font-size: 18px;
    line-height: 31px;
  }
  .identity .person-name {
    margin: 0 0 6px;
    color: var(--brand-orange);
    font-size: 37px;
    line-height: 44px;
    font-weight: 400;
  }
  .identity address { font-style: normal; }

  .brand-name {
    position: absolute;
    left: 96px;
    top: 212px;
    display: flex;
    align-items: center;
    gap: 12px;
    color: var(--brand-grey);
    font-size: 40px;
    line-height: 1;
  }
  .brand-name .dot {
    width: 26px;
    height: 26px;
    border-radius: 50%;
    background: var(--brand-orange);
  }

  .contact-line {
    position: absolute;
    top: 357px;
    font-size: 18px;
    display: flex;
    align-items: center;
    gap: 3px;
  }
  .contact-line--email { left: 43px; }
  .contact-line--social { right: 42px; }
  .contact-line .icon {
    width: 14px;
    height: 14px;
    border-radius: 2px;
    background: var(--icon-blue);
  }

  .back-circle {
    position: absolute;
    left: 200px;
    top: 70px;
    width: 290px;
    height: 290px;
    border-radius: 50%;
    background: var(--brand-peach);
  }
  .web-address {
    position: absolute;
    left: 0;
    right: 0;
    top: 190px;
    text-align: center;
    margin: 0;
    font-size: 45px;
    color: var(--ink-dark);
    font-weight: 400;
  }
</style>
</head>
<body>
<main class="sheet">
  <h2 class="side-label side-label--front">Front Side</h2>
  <section class="card card--front" aria-label="Card front">
    <p class="phones">
      <span class="kind">p</span>555.210.4830<br>
      <span class="kind">c</span>555.318.7726
    </p>
    <div class="identity">
      <h1 class="person-name">Martin Ellery</h1>
      <div class="job-title">President &amp; CEO</div>
      <address>2150 Alder Crest Road<br>Suite 118<br>Fairhollow, CA 93018</address>
    </div>
    <div class="brand-name"><span>Bramble Harbor</span><span class="dot"></span></div>
    <div class="contact-line contact-line--email"><span class="icon"></span>martinellery@brambleharbor.com</div>
    <div class="contact-line contact-line--social"><span class="icon"></span>martinellery</div>
  </section>

  <h2 class="side-label side-label--back">Back Side</h2>
  <section class="card card--back" aria-label="Card back">
    <div class="back-circle"></div>
    <p class="web-address">www.brambleharbor.com</p>
  </section>
</main>
</body>
</html>
```